Zielgruppe
leitwerkverleih.de vermietet Baustromverteiler an Bauunternehmen und private Bauherren.
Wir liefern die Verteiler, stellen sie auf und führen Terminabsprachen mit den örtlichen Energieversorgern.
Aufgabenstellung
-Nach Druckvorgabe Druckfalke ( Befestigung links)
-Logo soll groß zu sehen sein
Die Fahne kann schlicht gehalten werden. Gerne aber auch eigene Ideen mit einbringen.
- Unternehmensschrift: Titel Fira Sans , Schrift : Montserrat

```html
<!DOCTYPE html>
<html lang="de">
<head>
<meta charset="utf-8">
<title>leitwerkverleih.de – Fahne</title>
<link rel="stylesheet" href="https://fonts.googleapis.com/css2?family=Fira+Sans:wght@500&family=Montserrat:wght@500&display=swap">
<style>
  :root {
    --brand-blue: #145190;
    --brand-orange: #f29400;
    --paper: #ffffff;
    --canvas: #ffffff;
  }
  html, body {
    margin: 0;
    padding: 0;
    width: 1082px;
    height: 1200px;
    overflow: hidden;
    background: var(--canvas);
  }
  .canvas {
    position: relative;
    width: 1082px;
    height: 1200px;
  }
  .flag {
    position: absolute;
    top: 163px;
    width: 326px;
    height: 869px;
    background: var(--paper);
    overflow: hidden;
  }
  .flag--front { left: 143px; }
  .flag--back  { left: 587px; }

  /* Front side */
  .front-wordmark {
    position: absolute;
    left: 132px;
    top: 377px;
    width: 600px;
    height: 70px;
    margin-left: -300px;
    text-align: center;
    transform: rotate(-90deg);
    font-family: "Fira Sans", sans-serif;
    font-weight: 500;
    font-size: 58px;
    line-height: 70px;
    color: var(--brand-blue);
    white-space: nowrap;
  }
  .front-mark {
    position: absolute;
    left: 64px;
    top: 690px;
    width: 84px;
    height: 84px;
    background: var(--brand-blue);
  }
  .social-band {
    position: absolute;
    right: 0;
    top: 0;
    width: 86px;
    height: 100%;
    background: var(--brand-orange);
  }
  .social-band__text {
    position: absolute;
    left: 43px;
    top: 436px;
    width: 660px;
    margin-left: -330px;
    height: 30px;
    margin-top: -15px;
    transform: rotate(-90deg);
    text-align: center;
    font-family: "Montserrat", sans-serif;
    font-weight: 500;
    font-size: 18px;
    line-height: 30px;
    color: var(--paper);
    white-space: nowrap;
  }
  .social-band__dot {
    position: absolute;
    left: 33px;
    width: 20px;
    height: 20px;
    border: 2px solid var(--paper);
    border-radius: 50%;
    box-sizing: border-box;
  }
  .social-band__dot--top { top: 70px; background: var(--paper); }
  .social-band__dot--bottom { top: 792px; }

  /* Back side */
  .back-mark {
    position: absolute;
    left: 113px;
    top: 72px;
    width: 100px;
    height: 100px;
    background: var(--brand-blue);
  }
  .back-wordmark {
    position: absolute;
    left: 0;
    top: 272px;
    width: 100%;
    text-align: center;
    font-family: "Fira Sans", sans-serif;
    font-weight: 500;
    font-size: 29px;
    line-height: 40px;
    color: var(--brand-blue);
  }
  .back-swoosh {
    position: absolute;
    left: 0;
    top: 0;
  }
  .contact-list {
    position: absolute;
    left: 24px;
    top: 673px;
    margin: 0;
    padding: 0;
    list-style: none;
  }
  .contact-list__item {
    display: flex;
    align-items: center;
    height: 28px;
    margin-bottom: 30px;
    font-family: "Montserrat", sans-serif;
    font-weight: 500;
    font-size: 17px;
    color: var(--paper);
  }
  .contact-list__icon {
    width: 26px;
    height: 26px;
    margin-right: 14px;
    flex: none;
  }
</style>
</head>
<body>
<div class="canvas">

  <section class="flag flag--front" aria-label="Fahne Vorderseite">
    <div class="front-wordmark">leitwerkverleih.de</div>
    <div class="front-mark"></div>
    <div class="social-band">
      <span class="social-band__dot social-band__dot--top"></span>
      <div class="social-band__text">Besuchen Sie uns auch auf unseren Social Media Kanälen!</div>
      <span class="social-band__dot social-band__dot--bottom"></span>
    </div>
  </section>

  <section class="flag flag--back" aria-label="Fahne Rückseite">
    <div class="back-mark"></div>
    <div class="back-wordmark">leitwerkverleih.de</div>
    <svg class="back-swoosh" width="326" height="869" viewBox="0 0 326 869" aria-hidden="true">
      <polygon points="0,442 326,358 326,370 0,455" fill="var(--brand-orange)"/>
      <polygon points="0,462 326,378 326,869 0,869" fill="var(--brand-blue)"/>
    </svg>
    <ul class="contact-list">
      <li class="contact-list__item">
        <svg class="contact-list__icon" viewBox="0 0 26 26" aria-hidden="true">
          <g fill="none" stroke="#fff" stroke-width="2">
            <circle cx="13" cy="13" r="11"/>
            <ellipse cx="13" cy="13" rx="5" ry="11"/>
            <line x1="2" y1="13" x2="24" y2="13"/>
            <line x1="4" y1="7.5" x2="22" y2="7.5"/>
            <line x1="4" y1="18.5" x2="22" y2="18.5"/>
          </g>
        </svg>
        www.leitwerkverleih.de
      </li>
      <li class="contact-list__item">
        <svg class="contact-list__icon" viewBox="0 0 26 26" aria-hidden="true">
          <rect x="2" y="2" width="22" height="22" rx="5" fill="none" stroke="#fff" stroke-width="2"/>
        </svg>
        leitwerkverleih.de
      </li>
      <li class="contact-list__item">
        <svg class="contact-list__icon" viewBox="0 0 26 26" aria-hidden="true">
          <circle cx="13" cy="13" r="12" fill="#fff"/>
        </svg>
        @leitwerkverleih.de
      </li>
    </ul>
  </section>

</div>
</body>
</html>
```